I sell Finches---picture of White Finch Bird----

I raise and sell light color and white Finch - need card to give to Pet shops with my name - Lorna Pettigrew, address: 271 North Ardmore Ln. Santa Barbara, Ca. 93187 - phone - 805-479-3816. All birds raised and nourished in large outside aviary--very healthy and cared for. Would like card to be shiny red with bold print in Broadway font----purple bold print on red card. Design options open - you know best. Would like a picture or pictures of Finches - light or white in color.

Industry/Entity Type

Pet

Contact Information for Business Card

THE WREN KEEPER (LARGE, BOLD BROADWAY PRINT)

```html
<!DOCTYPE html>
<html lang="en">
<head>
<meta charset="utf-8">
<title>The Wren Keeper — Business Card</title>
<link rel="stylesheet" href="https://fonts.googleapis.com/css2?family=Limelight&display=swap">
<style>
  :root {
    --card-red: #ed1c24;
    --deco-purple: #662d91;
    --outline-white: #ffffff;
    --branch-brown: #6b5a4a;
    --bird-white: #f4f2f5;
  }
  * { margin: 0; padding: 0; box-sizing: border-box; }
  html, body {
    width: 1200px;
    height: 704px;
    overflow: hidden;
    background: var(--card-red);
  }
  .card {
    position: relative;
    width: 1200px;
    height: 704px;
    background: var(--card-red);
    overflow: hidden;
    font-family: "Limelight", "Times New Roman", serif;
    color: var(--deco-purple);
  }
  .side-panel {
    position: absolute;
    inset: 0;
    width: 1200px;
    height: 704px;
  }
  .outlined {
    color: var(--deco-purple);
    -webkit-text-stroke: 2px var(--outline-white);
    paint-order: stroke fill;
  }
  .brand-title {
    position: absolute;
    left: 48px;
    top: 42px;
    font-size: 80px;
    line-height: 1;
    letter-spacing: 1px;
    white-space: nowrap;
  }
  .owner-name {
    position: absolute;
    left: 50px;
    top: 188px;
    font-size: 54px;
    line-height: 1;
    letter-spacing: 1px;
    white-space: nowrap;
  }
  .name-rule {
    position: absolute;
    left: 50px;
    top: 260px;
    width: 592px;
    height: 3px;
    background: var(--outline-white);
  }
  .contact {
    position: absolute;
    left: 48px;
    font-size: 40px;
    line-height: 50px;
    white-space: nowrap;
  }
  .contact-address { top: 298px; }
  .contact-phone { top: 416px; }
  .contact-icon {
    position: absolute;
    left: 0;
    top: 9px;
    width: 34px;
    height: 34px;
  }
  .contact-text {
    display: block;
    padding-left: 50px;
    -webkit-text-stroke: 1.5px var(--outline-white);
    paint-order: stroke fill;
  }
  .address-line-2 { padding-left: 50px; }
  .promises {
    position: absolute;
    left: 46px;
    top: 496px;
    list-style: none;
    font-size: 38px;
    line-height: 50px;
    white-space: nowrap;
    -webkit-text-stroke: 1.5px var(--outline-white);
    paint-order: stroke fill;
  }
  .promises li { padding-left: 24px; text-indent: -24px; }
  .promises li::before {
    content: "•";
    display: inline-block;
    width: 24px;
    text-indent: 0;
    color: var(--outline-white);
    -webkit-text-stroke: 0;
  }
  .promise-gap { margin-top: 6px; }
</style>
</head>
<body>
<main class="card">
  <svg class="side-panel" viewBox="0 0 1200 704" aria-hidden="false">
    <defs>
      <clipPath id="panel-shape">
        <path d="M1125 0 C1075 160 1000 260 930 380 C880 460 870 580 900 704 L1200 704 L1200 0 Z"/>
      </clipPath>
      <radialGradient id="finch-glow" cx="0.55" cy="0.5" r="0.45">
        <stop offset="0" stop-color="#f4f2f5"/>
        <stop offset="0.55" stop-color="#c9b8d6"/>
        <stop offset="1" stop-color="#662d91" stop-opacity="0"/>
      </radialGradient>
      <linearGradient id="branch-tone" x1="0" y1="0" x2="1" y2="0">
        <stop offset="0" stop-color="#662d91" stop-opacity="0"/>
        <stop offset="0.7" stop-color="#6b5a4a" stop-opacity="0.6"/>
        <stop offset="1" stop-color="#6b5a4a"/>
      </linearGradient>
    </defs>
    <path class="panel-edge" d="M1125 0 C1075 160 1000 260 930 380 C880 460 870 580 900 704" fill="none" stroke="#ffffff" stroke-width="22"/>
    <path class="panel-fill" d="M1125 0 C1075 160 1000 260 930 380 C880 460 870 580 900 704 L1200 704 L1200 0 Z" fill="#662d91"/>
    <g class="finch-photo" role="img" aria-label="Photo of a white finch with a red beak perched on a bare branch" clip-path="url(#panel-shape)">
      <rect x="880" y="0" width="320" height="704" fill="url(#branch-tone)" opacity="0.55"/>
      <rect x="880" y="200" width="320" height="480" fill="url(#finch-glow)"/>
    </g>
  </svg>

  <h1 class="brand-title outlined">THE WREN KEEPER</h1>
  <h2 class="owner-name outlined">LORNA PETTIGREW</h2>
  <div class="name-rule"></div>

  <address class="contact contact-address" style="font-style:normal">
    <svg class="contact-icon" viewBox="0 0 34 34" aria-hidden="true">
      <circle cx="17" cy="17" r="16" fill="#ffffff"/>
      <path d="M17 7 a7 7 0 0 1 7 7 c0 5 -7 12 -7 12 s-7 -7 -7 -12 a7 7 0 0 1 7 -7 z" fill="#662d91"/>
      <circle cx="17" cy="14" r="2.6" fill="#ffffff"/>
    </svg>
    <span class="contact-text">271 North Ardmore Ln.</span>
    <span class="contact-text address-line-2">Santa Barbara, Ca. 93187</span>
  </address>

  <div class="contact contact-phone">
    <svg class="contact-icon" viewBox="0 0 34 34" aria-hidden="true">
      <circle cx="17" cy="17" r="16" fill="#ffffff"/>
      <path d="M11 9 l4 0 l1.5 5 l-2.5 2 c1 2.5 3 4.5 5.5 5.5 l2 -2.5 l5 1.5 l0 4 c0 1 -1 2 -2 2 c-8 -0.5 -14 -6.5 -14.5 -14.5 c0 -1 1 -2 1 -3 z" fill="#662d91"/>
    </svg>
    <span class="contact-text">805-479-3816</span>
  </div>

  <ul class="promises">
    <li>All birds raised and nourished<br>in large outside aviary</li>
    <li class="promise-gap">very healthy and cared for.</li>
  </ul>
</main>
</body>
</html>
```